New Business Cards for Torvin Group

We need a new Business Card to compliment our new logo. We are a vibrant design, manufacture and install business providing recreation areas, public parks and Municipal spaces. We want business cards that are classy, modern and clean.

We have recently changed our logo, and are celebrating our 40th anniversary. We want business cards with a new modern design to reflect our status.

Target Market(s)

Customers

Contact Information for Business Card

We need all the details of our 3 offices as per the business card attached. Please disregard the old logo on the business card, the other three files show our new logo.

Requirements
Must have
• All info as per attached business card but with new logo.
Nice to have

```html
<!DOCTYPE html>
<html lang="en">
<head>
<meta charset="utf-8">
<title>Torvin Group Business Cards</title>
<link href="https://fonts.googleapis.com/css2?family=Arimo:wght@400;700&display=swap" rel="stylesheet">
<style>
:root{
  --red:#d8323c;
  --red-dark:#bf2430;
  --red-light:#e5525a;
  --ink:#4a4a4a;
  --grey:#6b6b6b;
  --paper:#f6f6f6;
  --stage:#e9e6e1;
  --white:#ffffff;
}
*{margin:0;padding:0;box-sizing:border-box}
html,body{width:1200px;height:780px;overflow:hidden}
body{background:var(--stage);font-family:"Arimo",Arial,sans-serif;position:relative}
.card{position:absolute;width:540px;height:320px;border-radius:18px;overflow:hidden;box-shadow:0 6px 18px rgba(0,0,0,.18)}
.card-front{left:40px;top:230px;background:var(--red)}
.card-back{left:620px;top:230px;background:linear-gradient(135deg,var(--red-light),var(--red-dark))}
.card-art{position:absolute;inset:0;width:100%;height:100%}
.holder{position:absolute;right:24px;top:8px;text-align:right;color:var(--white)}
.holder-name{font-weight:700;font-size:17px;letter-spacing:.3px}
.holder-title{font-size:11px;margin-top:2px}
.brand{position:absolute;display:flex;align-items:center;gap:10px}
.brand-front{left:150px;top:160px}
.brand-mark{flex:0 0 auto;width:46px;height:46px;border-radius:50%;background:var(--red)}
.brand-name{font-weight:700;font-size:27px;color:var(--ink);letter-spacing:.5px;text-transform:uppercase;white-space:nowrap}
.direct{position:absolute;left:310px;top:98px;font-size:10.5px;line-height:16px;color:var(--grey);white-space:nowrap}
.direct .web{letter-spacing:2px}
.offices{position:absolute;left:84px;top:228px;display:flex;gap:12px}
.office{width:136px}
.office-title{font-size:13px;color:var(--ink);padding-bottom:4px;border-bottom:1px solid var(--red);margin-bottom:5px;white-space:nowrap}
.office-line{font-size:8.5px;line-height:12px;color:var(--grey);white-space:nowrap}
.map-fill{position:absolute;left:60px;top:40px;width:430px;height:250px;border-radius:40px;background:radial-gradient(ellipse at center,rgba(255,255,255,.16),rgba(255,255,255,.04) 70%)}
.brand-back{left:50%;top:50%;transform:translate(-50%,-60%)}
.brand-back .brand-mark{background:transparent;border:4px solid var(--white);width:58px;height:58px}
.brand-back .brand-name{color:var(--white);font-size:34px}
.back-web{position:absolute;left:0;right:0;top:206px;text-align:center;color:var(--white);font-size:11px;letter-spacing:2.5px}
</style>
</head>
<body>
<section class="card card-front">
  <svg class="card-art" viewBox="0 0 540 320" aria-hidden="true">
    <path d="M10 320 C40 170 250 60 540 56 L540 320 Z" fill="var(--paper)"/>
    <path d="M-2 310 C30 160 248 44 540 40 L540 47 C252 52 40 166 6 318 Z" fill="var(--grey)"/>
  </svg>
  <div class="holder">
    <div class="holder-name">Milo Haskett</div>
    <div class="holder-title">Managing Partner</div>
  </div>
  <div class="brand brand-front">
    <span class="brand-mark"></span>
    <span class="brand-name">Torvin Group</span>
  </div>
  <div class="direct">
    <div>M : +971 (0)50 384 7102</div>
    <div>E: milo@torvingroup.com</div>
    <div class="web">www.torvingroup.com</div>
  </div>
  <div class="offices">
    <div class="office">
      <div class="office-title">Head Office</div>
      <div class="office-line">P.O. Box 41820 Abu Dhabi, U.A.E.</div>
      <div class="office-line">Tel No: +971 (0)2 5831207</div>
      <div class="office-line">Fax No: +971 (0)2 5831208</div>
      <div class="office-line">Email: sales@torvingroup.com</div>
    </div>
    <div class="office">
      <div class="office-title">Dubai Office</div>
      <div class="office-line">P.O. Box 270614 Dubai, U.A.E.</div>
      <div class="office-line">Tel No: +971 (0)4 3906425</div>
      <div class="office-line">Fax No: +971 (0)4 3906426</div>
      <div class="office-line">Email: sales@torvingroup.com</div>
    </div>
    <div class="office">
      <div class="office-title">Qatar Office</div>
      <div class="office-line">P.O. Box 58903 Doha, Qatar</div>
      <div class="office-line">Tel No: +974 44718290</div>
      <div class="office-line">Fax No: +974 44718291</div>
      <div class="office-line">Email: sales@torvingroup.com</div>
    </div>
  </div>
</section>

<section class="card card-back">
  <div class="map-fill" role="img" aria-label="Faint world map in light red tones"></div>
  <div class="brand brand-back">
    <span class="brand-mark"></span>
    <span class="brand-name">Torvin Group</span>
  </div>
  <div class="back-web">www.torvingroup.com</div>
</section>
</body>
</html>
```